Header Design

I would like a new header design for my website - www.nestmarla.com.

I am a Realtor and the header should reflect that and complement the theme.

The attached logo needs to be included and the information that is already there. Also, the colors need to match.

Marla Quinby
Connecting you to the Los Angeles real estate scene.

Industry/Entity Type

Realtor

```html
<!DOCTYPE html>
<html lang="en">
<head>
<meta charset="utf-8">
<title>Marla Quinby – Los Angeles Real Estate</title>
<link rel="stylesheet" href="https://fonts.googleapis.com/css2?family=Great+Vibes&family=Open+Sans:wght@300;400&display=swap">
<style>
  :root {
    --plum: #3a1f3d;
    --white: #ffffff;
    --tab: #f1f1f1;
    --tab-text: #555555;
    --soft-white: #ece6ee;
  }
  * { margin: 0; padding: 0; box-sizing: border-box; }
  html, body { width: 1200px; height: 126px; overflow: hidden; background: var(--white); }
  .site-header {
    position: relative;
    width: 1200px;
    height: 126px;
    background: var(--plum);
    font-family: "Open Sans", Arial, sans-serif;
    color: var(--soft-white);
  }
  .brand-mark {
    position: absolute;
    left: 14px;
    top: 28px;
    width: 110px;
    display: flex;
    align-items: center;
    gap: 7px;
  }
  .brand-square {
    width: 16px;
    height: 16px;
    background: var(--white);
    flex: none;
  }
  .brand-name {
    font-weight: 300;
    font-size: 13px;
    line-height: 1.25;
    text-transform: uppercase;
    color: var(--white);
  }
  .divider {
    position: absolute;
    left: 137px;
    top: 0;
    width: 1px;
    height: 126px;
    background: var(--soft-white);
  }
  .site-title {
    position: absolute;
    left: 178px;
    top: 20px;
    font-family: "Great Vibes", cursive;
    font-weight: 400;
    font-size: 48px;
    line-height: 1;
    color: var(--white);
    white-space: nowrap;
    transform: scaleX(0.6);
    transform-origin: left center;
  }
  .tagline {
    position: absolute;
    left: 530px;
    top: 40px;
    font-weight: 300;
    font-size: 13.5px;
    text-transform: uppercase;
    white-space: nowrap;
  }
  .phone-tab {
    position: absolute;
    right: 0;
    top: 0;
    width: 226px;
    height: 38px;
    background: var(--tab);
    border-bottom-left-radius: 26px;
    display: flex;
    align-items: center;
    padding-left: 28px;
    gap: 6px;
    color: var(--tab-text);
    font-size: 17px;
    font-weight: 300;
  }
  .phone-icon { width: 24px; height: 24px; }
  .main-nav {
    position: absolute;
    left: 192px;
    top: 90px;
    display: flex;
    align-items: center;
    white-space: nowrap;
  }
  .nav-item {
    font-size: 15px;
    font-weight: 300;
    text-transform: uppercase;
    color: var(--soft-white);
    text-decoration: none;
    padding: 0 9px;
    border-left: 1px solid var(--soft-white);
    line-height: 17px;
  }
  .nav-home { padding: 0 14px 0 0; border: none; display: flex; }
  .home-icon { width: 28px; height: 24px; }
</style>
</head>
<body>
<header class="site-header">
  <div class="brand-mark">
    <span class="brand-square"></span>
    <span class="brand-name">Marla<br>Quinby</span>
  </div>
  <div class="divider"></div>

  <h1 class="site-title">MARLA QUINBY</h1>
  <p class="tagline">Connecting you to the Los Angeles real estate scene</p>

  <div class="phone-tab">
    <svg class="phone-icon" viewBox="0 0 24 24" fill="none" stroke="#555555" stroke-width="1.3" stroke-linejoin="round">
      <path d="M6.5 2.5l3 4.5-2 2c1 2.6 3.2 4.8 5.5 5.8l2-2 4.5 3-1.8 3.2c-7-.5-12.8-6.3-13.2-13.3z"/>
      <path d="M14 3.5a7 7 0 0 1 6.5 6.5M14 7a3.5 3.5 0 0 1 3 3"/>
    </svg>
    <span class="phone-number">- 310 555 0142</span>
  </div>

  <nav class="main-nav">
    <a class="nav-home" href="#" aria-label="Home">
      <svg class="home-icon" viewBox="0 0 28 24" fill="none" stroke="#ece6ee" stroke-width="1.4" stroke-linejoin="round">
        <path d="M2 12L14 2l12 10"/>
        <path d="M6 9v13h6v-7h4v7h6V9"/>
      </svg>
    </a>
    <a class="nav-item" href="#">About Marla</a>
    <a class="nav-item" href="#">Home&nbsp; Searc Central</a>
    <a class="nav-item" href="#">Search by Community</a>
    <a class="nav-item" href="#">Buyers</a>
    <a class="nav-item" href="#">Sellers</a>
    <a class="nav-item" href="#">Renters</a>
    <a class="nav-item" href="#">Market Reports</a>
    <a class="nav-item" href="#">Contact Me</a>
  </nav>
</header>
</body>
</html>
```